Rising Paths Web Design

I am starting a new company that will provide LIFE COACHING services - I have tried to design a website, but it's too complicated. Right now, it's just me - I'm the only person that will provide services through the website - I have used artmarket to purchase a logo (see below). I want to be able to update the website myself, but need a template - basic design. Because I am not technologically savvy enough to explain in words - I basically want to have a website that will provide basic information about my services (coaching), a page about me and my background, hopefully scheduling possibilities, and testimonials — also a page for writing/blogs. I bought a website through NetHarbor - so when I have a template, I guess I”d use that - but maybe I’ll need to work with a designer to actually get it up on the internet. I have a head shot that I’ll upload, too.
Target Market(s)
Clients from the independent (private school) world - teachers, administrators
Number of Pages Required
4 page
Look and feel
Each slider illustrates characteristics of the customer's brand and the style your logo design should communicate.

```html
<!DOCTYPE html>
<html lang="en">
<head>
<meta charset="utf-8">
<title>Rising Paths Coaching</title>
<link href="https://fonts.googleapis.com/css2?family=Nunito:wght@400;600;700;800&display=swap" rel="stylesheet">
<style>
:root{
  --teal:#0fb8a0;
  --teal-deep:#0aa88f;
  --teal-bright:#14c2a8;
  --mint:#e8f7f3;
  --ink:#3b3b3b;
  --text:#555;
  --dark:#434343;
  --white:#fff;
}
*{margin:0;padding:0;box-sizing:border-box}
html,body{width:1200px;height:3555px;overflow:hidden}
body{font-family:'Nunito',sans-serif;color:var(--text);background:var(--white);position:relative}
.abs{position:absolute}
.btn{position:absolute;display:flex;align-items:center;justify-content:center;border-radius:22px;font-weight:800;font-size:14px;color:var(--white);text-transform:uppercase;letter-spacing:.2px}
.btn-dark{background:var(--ink)}
.btn-teal{background:var(--teal)}
.pager{position:absolute;display:flex;align-items:center;gap:8px;font-size:12px;font-weight:600;color:var(--ink)}
.pager svg{width:32px;height:10px}
.brand{position:absolute;display:flex;align-items:center;gap:10px;font-weight:700;letter-spacing:1px}
.brand .dot{width:22px;height:22px;border:2px solid var(--teal);border-radius:50%}

/* header */
.topbar{top:22px;right:50px;display:flex;gap:40px;font-size:13px;color:var(--ink)}
.topbar span{display:flex;align-items:center;gap:10px}
.topbar b{font-weight:800;font-size:15px}
.nav{top:74px;left:410px;display:flex;gap:28px;font-size:13px;color:var(--ink)}
.nav .active{color:var(--teal)}

/* hero */
.hero-band{top:220px;left:0;width:1200px;height:446px;background:var(--mint)}
.hero-photo{top:138px;left:593px;width:607px;height:528px;background:linear-gradient(100deg,rgba(232,247,243,0) 0%,#d9b49b 22%,#c99677 45%,#efe6dc 75%,#f6f2ec 100%)}
.hero-title{top:282px;left:45px;font-size:50px;line-height:62px;color:var(--ink);font-weight:400}
.hero-title strong{color:var(--teal);font-weight:800;display:block}
.hero-lead{top:413px;left:45px;width:560px;font-size:17px;line-height:26px;color:var(--ink)}

/* services */
.service{position:absolute;background:var(--teal-deep);color:var(--white);padding:32px 25px}
.service.feature{background:var(--teal-bright);box-shadow:0 6px 18px rgba(0,0,0,.15)}
.service h3{font-size:26px;font-weight:700;margin-bottom:12px}
.service p{font-size:13px;line-height:20px}
.service .btn{font-size:13px}

/* about */
.about-photo{top:1165px;left:178px;width:440px;height:480px;border-radius:50%;background:radial-gradient(ellipse at 50% 40%,#f0d9c4 0%,#e3c39f 35%,#d9c79f 55%,#efe9df 80%)}
.about-ring{top:1190px;left:160px;width:470px;height:480px}
.about-kicker{top:1208px;left:680px;font-size:38px;color:var(--ink)}
.about-title{top:1251px;left:680px;font-size:38px;font-weight:800;color:var(--teal)}
.about-text{left:680px;width:365px;font-size:13px;line-height:20px;color:var(--text)}
.signature{top:1478px;left:680px;width:210px;height:56px;background:linear-gradient(90deg,#f4f4f4,#ececec);border-radius:4px}

/* testimonials */
.testi-band{top:1746px;left:0;width:1200px;height:480px;background:var(--teal)}
.testi-photo{top:1746px;left:0;width:538px;height:480px;background:linear-gradient(160deg,#c9b9a6 0%,#b78763 35%,#6b4a36 60%,#a8896d 85%,#8a6a50 100%)}
.testi-title{top:1805px;left:593px;font-size:38px;font-weight:800;color:var(--white)}
.quote{position:absolute;top:1885px;width:266px;height:131px;background:var(--mint);border-radius:14px;padding:24px 24px;font-size:13px;line-height:20px;color:var(--ink)}
.quote::after{content:"";position:absolute;left:34px;bottom:-20px;border-right:22px solid transparent;border-top:22px solid var(--mint)}
.client{position:absolute;top:2061px;font-size:14px;font-weight:700;color:var(--ink)}
.stars{position:absolute;top:2082px;font-size:16px;letter-spacing:6px;color:var(--ink)}

/* blogs */
.blogs-title{top:2298px;left:0;width:1200px;text-align:center;font-size:38px;color:var(--ink)}
.blogs-title strong{color:var(--teal);font-weight:800}
.post{position:absolute;top:2379px;width:350px;height:473px;border:2px solid var(--teal);background:var(--white)}
.post-img{height:248px;position:relative}
.post-plus{position:absolute;top:16px;left:14px;width:40px;height:40px;background:var(--teal);display:flex;align-items:center;justify-content:center}
.post h4{margin:26px 22px 10px;font-size:27px;line-height:31px;font-weight:600;color:var(--ink)}
.post p{margin:0 22px;font-size:13px;line-height:20px;color:var(--text)}
.post-meta{margin:16px 22px 0;display:flex;gap:22px;font-size:11px;color:var(--ink);text-transform:uppercase}
.post-meta span{display:flex;align-items:center;gap:6px}

/* contact */
.contact-band{top:2988px;left:0;width:1200px;height:239px;background:var(--teal)}
.contact-side{top:2988px;left:734px;width:466px;height:239px;background:var(--teal-deep)}
.contact-title{top:3053px;left:175px;font-size:34px;color:var(--white);font-weight:400}
.btn-white{background:var(--white);color:var(--ink);font-size:19px;border-radius:24px}
.contact-list{top:3042px;left:777px;color:var(--white);font-size:15px;line-height:20px}
.contact-list .row{display:flex;gap:16px;margin-bottom:12px;align-items:flex-start}
.contact-list .phone{font-size:23px;font-weight:800}

/* footer */
.footer{top:3227px;left:0;width:1200px;height:328px;background:var(--dark)}
.footer-ring{top:3295px;left:180px;width:170px;height:170px;border:2px solid var(--teal);border-radius:50%}
.fcol{top:3298px;font-size:13px;line-height:21px;color:var(--white)}
.fcol h5{font-size:18px;color:var(--teal);font-weight:700;margin-bottom:10px}
.copyright{top:3500px;left:178px;font-size:12px;color:var(--white)}
.social{position:absolute;top:3486px;width:36px;height:36px;border-radius:50%;background:var(--teal)}
</style>
</head>
<body>

<!-- header -->
<div class="brand" style="top:92px;left:56px;font-size:24px;color:var(--ink)"><span class="dot"></span>RISING PATHS</div>
<div class="topbar abs">
  <span><svg width="20" height="20" viewBox="0 0 24 24" fill="none" stroke="#0fb8a0" stroke-width="1.6"><path d="M5 3h4l2 5-2.5 1.5a11 11 0 0 0 6 6L16 13l5 2v4a2 2 0 0 1-2 2A16 16 0 0 1 3 5a2 2 0 0 1 2-2z"/></svg>Call us - <b>+1 555 014 2290</b></span>
  <span><svg width="20" height="16" viewBox="0 0 24 18" fill="none" stroke="#0fb8a0" stroke-width="1.6"><rect x="1" y="1" width="22" height="16"/><path d="M1 1l11 9 11-9"/></svg>Emai us - info@risingpaths.com</span>
</div>
<nav class="nav abs"><span class="active">HOME</span><span>ABOUT</span><span>SERVICES</span><span>COACHING</span><span>BLOG</span><span>CONTACT</span></nav>
<div class="btn btn-dark" style="top:62px;left:898px;width:256px;height:39px">Schedule an appointment</div>

<!-- hero -->
<div class="hero-band abs"></div>
<div class="hero-photo abs" role="img" aria-label="Smiling mother hugging her young daughter"></div>
<svg class="abs" style="top:175px;left:640px" width="460" height="450" viewBox="0 0 460 450" fill="none" stroke="#0fb8a0" stroke-width="2"><circle cx="230" cy="225" r="200"/></svg>
<h1 class="hero-title abs"><strong>Taking Care</strong>of Your Life Issues!</h1>
<p class="hero-lead abs">Get the motivation, guidance, and support you need to get your life on track. You don't need to struggle on your own anymore!</p>
<div class="btn btn-teal" style="top:495px;left:45px;width:291px;height:40px">Schedule an appointment</div>
<div class="pager" style="top:619px;left:45px"><svg viewBox="0 0 32 10" fill="none" stroke="#3b3b3b"><path d="M31 5H1M5 1L1 5l4 4"/></svg>PREV</div>
<div class="pager" style="top:619px;left:136px">NEXT<svg viewBox="0 0 32 10" fill="none" stroke="#3b3b3b"><path d="M1 5h30M27 1l4 4-4 4"/></svg></div>

<!-- services -->
<div class="service" style="top:775px;left:47px;width:370px;height:226px">
  <h3>Consultancy &amp; Advicing</h3>
  <p>Lorem ipsum dolor sit amet, consectetur adipiscing elit, sed do eiusmod tempor incididunt ut labore et dolore magna aliqua.</p>
  <div class="btn btn-dark" style="top:157px;left:26px;width:134px;height:34px">Read more</div>
</div>
<div class="service" style="top:775px;left:786px;width:368px;height:226px">
  <h3>Conferencing &amp; Talks</h3>
  <p>Lorem ipsum dolor sit amet, consectetur adipiscing elit, sed do eiusmod tempor incididunt ut labore et dolore magna aliqua.</p>
  <div class="btn btn-dark" style="top:157px;left:26px;width:134px;height:34px">Read more</div>
</div>
<div class="service feature" style="top:761px;left:417px;width:370px;height:254px">
  <h3>Problem Solving</h3>
  <p>Lorem ipsum dolor sit amet, consectetur adipiscing elit, sed do eiusmod tempor incididunt ut labore et dolore magna aliqua. Ut enim ad minim veniam, quis nostrud exercitation ullamco laboris nisi ut aliquip .</p>
  <div class="btn btn-dark" style="top:186px;left:26px;width:134px;height:34px">Read more</div>
</div>

<!-- about -->
<div class="about-photo abs" role="img" aria-label="Portrait of the coach, smiling, in a cream turtleneck"></div>
<svg class="about-ring abs" viewBox="0 0 470 480" fill="none" stroke="#0fb8a0" stroke-width="2"><circle cx="235" cy="250" r="222"/></svg>
<div class="about-kicker abs">Rising Paths</div>
<div class="about-title abs">Transforms Lives</div>
<p class="about-text abs" style="top:1317px">Lorem ipsum dolor sit amet, consectetur adipiscing elit, sed do eiusmod tempor incididunt ut labore et dolore magna aliqua. Ut enim ad minim veniam, quis nostrud exercitation ullamco laboris nisi ut aliquip ex ea commodo consequat.</p>
<p class="about-text abs" style="top:1413px">Duis aute irure dolor in reprehenderit in voluptate velit esse cillum dolore eu fugiat nulla pariatur.</p>
<div class="signature abs" role="img" aria-label="Handwritten signature"></div>
<div class="btn btn-teal" style="top:1573px;left:683px;width:161px;height:39px">About us</div>

<!-- testimonials -->
<div class="testi-band abs"></div>
<div class="testi-photo abs" role="img" aria-label="Smiling couple at a café counter with a tablet"></div>
<div class="testi-title abs">Happy Client's</div>
<div class="quote" style="left:594px">Lorem ipsum dolor sit amet, consectetur adipiscing elit, sed do eiusmod tempor incididunt ut labore et dolore magna aliqua.</div>
<div class="quote" style="left:887px">Lorem ipsum dolor sit amet, consectetur adipiscing elit, sed do eiusmod tempor incididunt ut labore et dolore magna aliqua.</div>
<div class="client" style="left:614px">LENA HART</div>
<div class="stars" style="left:614px">★★★★★</div>
<div class="client" style="left:907px">LENA HART</div>
<div class="stars" style="left:907px">★★★★★</div>
<div class="pager" style="top:2151px;left:594px"><svg viewBox="0 0 32 10" fill="none" stroke="#3b3b3b"><path d="M31 5H1M5 1L1 5l4 4"/></svg>PREV</div>
<div class="btn btn-dark" style="top:2140px;left:784px;width:182px;height:34px;font-size:13px">All testimonials</div>
<div class="pager" style="top:2151px;left:1082px">NEXT<svg viewBox="0 0 32 10" fill="none" stroke="#3b3b3b"><path d="M1 5h30M27 1l4 4-4 4"/></svg></div>

<!-- blogs -->
<h2 class="blogs-title abs">Latest <strong>Blogs</strong></h2>
<article class="post" style="left:46px">
  <div class="post-img" role="img" aria-label="Person relaxing at a desk in front of a computer" style="background:linear-gradient(180deg,#ece9e4 0%,#d9d3ca 40%,#c8892f 70%,#a9742e 100%)"><div class="post-plus"><svg width="24" height="24" stroke="#fff" stroke-width="2"><path d="M12 2v20M2 12h20"/></svg></div></div>
  <h4>Thoughts on Procrastination</h4>
  <p>Lorem ipsum dolor sit amet, consectetur adipiscing elit, sed do eiusmod tempor incididunt ut labore et dolore magna aliqua.</p>
  <div class="post-meta"><span><svg width="11" height="11" viewBox="0 0 12 12" fill="none" stroke="#0fb8a0"><rect x=".5" y="1.5" width="11" height="10"/><path d="M.5 4.5h11"/></svg>January 12, 2018</span><span><svg width="11" height="11" viewBox="0 0 12 12" fill="none" stroke="#0fb8a0"><circle cx="6" cy="4" r="3"/><path d="M1 12a5 5 0 0 1 10 0"/></svg>By Marcus</span></div>
</article>
<article class="post" style="left:425px">
  <div class="post-img" role="img" aria-label="Group of kitchen staff posing together" style="background:linear-gradient(180deg,#55504c 0%,#8b8581 35%,#e4e1dd 60%,#7a5a44 100%)"><div class="post-plus"><svg width="24" height="24" stroke="#fff" stroke-width="2"><path d="M12 2v20M2 12h20"/></svg></div></div>
  <h4>People who made inspiring life changes</h4>
  <p>Lorem ipsum dolor sit amet, consectetur adipiscing elit, sed do eiusmod tempor incididunt ut labore et dolore magna aliqua.</p>
  <div class="post-meta"><span><svg width="11" height="11" viewBox="0 0 12 12" fill="none" stroke="#0fb8a0"><rect x=".5" y="1.5" width="11" height="10"/><path d="M.5 4.5h11"/></svg>January 12, 2018</span><span><svg width="11" height="11" viewBox="0 0 12 12" fill="none" stroke="#0fb8a0"><circle cx="6" cy="4" r="3"/><path d="M1 12a5 5 0 0 1 10 0"/></svg>By Marcus</span></div>
</article>
<article class="post" style="left:804px">
  <div class="post-img" role="img" aria-label="People walking hand in hand across a green field at sunset" style="background:linear-gradient(180deg,#d7c79a 0%,#8aa55a 35%,#4f8a2c 65%,#2f6b1c 100%)"><div class="post-plus"><svg width="24" height="24" stroke="#fff" stroke-width="2"><path d="M12 2v20M2 12h20"/></svg></div></div>
  <h4>The incredible power of small changes</h4>
  <p>Lorem ipsum dolor sit amet, consectetur adipiscing elit, sed do eiusmod tempor incididunt ut labore et dolore magna aliqua.</p>
  <div class="post-meta"><span><svg width="11" height="11" viewBox="0 0 12 12" fill="none" stroke="#0fb8a0"><rect x=".5" y="1.5" width="11" height="10"/><path d="M.5 4.5h11"/></svg>January 12, 2018</span><span><svg width="11" height="11" viewBox="0 0 12 12" fill="none" stroke="#0fb8a0"><circle cx="6" cy="4" r="3"/><path d="M1 12a5 5 0 0 1 10 0"/></svg>By Marcus</span></div>
</article>
<div class="pager" style="top:2915px;left:45px"><svg viewBox="0 0 32 10" fill="none" stroke="#3b3b3b"><path d="M31 5H1M5 1L1 5l4 4"/></svg>PREV</div>
<div class="btn btn-dark" style="top:2905px;left:534px;width:132px;height:34px;font-size:13px">View all</div>
<div class="pager" style="top:2915px;left:1082px">NEXT<svg viewBox="0 0 32 10" fill="none" stroke="#3b3b3b"><path d="M1 5h30M27 1l4 4-4 4"/></svg></div>

<!-- contact -->
<div class="contact-band abs"></div>
<div class="contact-side abs"></div>
<div class="contact-title abs">FEEL FREE TO CONTACT US</div>
<div class="btn btn-white" style="top:3112px;left:178px;width:356px;height:43px">SCHEDULE AN APPOINTMENT</div>
<div class="contact-list abs">
  <div class="row phone"><svg width="28" height="28" viewBox="0 0 24 24" fill="none" stroke="#fff" stroke-width="1.6"><path d="M5 3h4l2 5-2.5 1.5a11 11 0 0 0 6 6L16 13l5 2v4a2 2 0 0 1-2 2A16 16 0 0 1 3 5a2 2 0 0 1 2-2z"/></svg>+1 555 014 2290</div>
  <div class="row"><svg width="16" height="20" viewBox="0 0 16 20" fill="#fff"><path d="M8 0a7 7 0 0 0-7 7c0 5 7 13 7 13s7-8 7-13a7 7 0 0 0-7-7zm0 10a3 3 0 1 1 0-6 3 3 0 0 1 0 6z"/></svg><span>48 Willow Lane, Brookfield.<br>BF 2RL</span></div>
  <div class="row"><svg width="16" height="12" viewBox="0 0 24 18" fill="none" stroke="#fff" stroke-width="2"><rect x="1" y="1" width="22" height="16"/><path d="M1 1l11 9 11-9"/></svg>info@risingpaths.com</div>
</div>

<!-- footer -->
<div class="footer abs"></div>
<div class="footer-ring abs"></div>
<div class="brand" style="top:3366px;left:190px;font-size:22px;color:var(--white)">RISING PATHS</div>
<div class="fcol abs" style="left:466px"><h5>Office Hours</h5>Mon - Wed : 8am - 7pm<br>Thursday : 8am - 5pm<br>Friday : 8am - 6pm<br>Sat - Sun : Closed</div>
<div class="fcol abs" style="left:687px"><h5>Usefull Links</h5>About<br>Coaching<br>Blog<br>Privacy Policy<br>Terms &amp; Conditions</div>
<div class="fcol abs" style="left:883px"><h5>Services</h5>Consultancy &amp; Advicing<br>Problem Solving<br>Conferencing &amp; Talks</div>
<div class="copyright abs">Copyright © <b>Rising Paths</b> 2022. All Right Reserved</div>
<span class="social" style="left:894px" aria-label="Social profile one"></span>
<span class="social" style="left:946px" aria-label="Social profile two"></span>
<span class="social" style="left:998px" aria-label="Social profile three"></span>

</body>
</html>
```